Business card for STEADYLINE

Please design professional business card for IT consulting firm STEADYLINE INC.
Use logo attached.
Use information from sample tRove business card attached.
replace trove inc with STEADYLINE INC.
as well as troveinc.com with steadyline.example

```html
<!DOCTYPE html>
<html lang="en">
<head>
<meta charset="utf-8">
<title>STEADYLINE INC. business card</title>
<link rel="stylesheet" href="https://fonts.googleapis.com/css2?family=Montserrat:wght@400;600;700&family=Roboto:wght@300;400&display=swap">
<style>
  :root {
    --backdrop: #231f20;
    --card: #ffffff;
    --ink: #111111;
    --text: #3a3a3a;
    --muted: #555555;
    --tint-strong: #dcdcdc;
    --tint-soft: #f4f4f4;
  }
  * { margin: 0; padding: 0; box-sizing: border-box; }
  html, body { width: 1200px; height: 1200px; overflow: hidden; background: var(--backdrop); }
  .stage { position: relative; width: 1200px; height: 1200px; }
  .card {
    position: absolute; left: 234px; width: 726px;
    background: var(--card); overflow: hidden;
    box-shadow: 2px 3px 6px rgba(0,0,0,.45);
  }
  .card--front { top: 165px; height: 415px; }
  .card--back { top: 618px; height: 419px; }
  .tint-square {
    position: absolute;
    background: radial-gradient(circle at 50% 55%, var(--tint-strong), var(--tint-soft) 95%);
  }
  .card--front .tint-square { left: 470px; top: 70px; width: 250px; height: 250px; }
  .card--back .tint-square { left: 80px; top: 80px; width: 260px; height: 260px; }
  .wordmark {
    position: absolute; font-family: "Montserrat", sans-serif; font-weight: 700;
    color: var(--ink); letter-spacing: .06em; white-space: nowrap; line-height: 1;
  }
  .card--front .wordmark { left: 49px; top: 64px; font-size: 40px; }
  .card--back .wordmark { left: 0; right: 0; top: 183px; text-align: center; font-size: 50px; }
  .details { position: absolute; left: 50px; top: 155px; font-family: "Roboto", sans-serif; color: var(--text); }
  .person-name { font-family: "Montserrat", sans-serif; font-weight: 600; font-size: 25px; color: var(--ink); line-height: 1; white-space: nowrap; }
  .person-name .credential { font-size: 16px; }
  .person-role { font-weight: 300; font-size: 17px; color: var(--muted); letter-spacing: .03em; margin-top: 6px; }
  .contact-grid { display: grid; grid-template-columns: 244px auto; row-gap: 10px; margin-top: 20px; font-size: 16px; white-space: nowrap; }
  .company-name { font-family: "Montserrat", sans-serif; font-weight: 600; font-size: 17px; color: var(--ink); margin-top: 15px; }
  .address { font-size: 16px; line-height: 21px; margin-top: 4px; }
</style>
</head>
<body>
<main class="stage">
  <section class="card card--front">
    <div class="tint-square"></div>
    <div class="wordmark">STEADYLINE INC.</div>
    <div class="details">
      <h1 class="person-name">DANIEL MORROW, <span class="credential">P. ENG.</span></h1>
      <p class="person-role">GENERAL MANAGER</p>
      <div class="contact-grid">
        <span>o.(555) 014-2290 EXT.201</span>
        <span>c.(555) 013-7745</span>
        <span>e.dmorrow@steadyline.example</span>
        <span>www.steadyline.example</span>
      </div>
      <h2 class="company-name">STEADYLINE INC.</h2>
      <p class="address">1280 Harbourview Rd, Suite 204<br>Lakeport, Ontario, L2X 4K8, Canada</p>
    </div>
  </section>
  <section class="card card--back">
    <div class="tint-square"></div>
    <div class="wordmark">STEADYLINE INC.</div>
  </section>
</main>
</body>
</html>
```